Maplerise Trading Inc. needs an innovative idea for letterhead and visiting cards.

Maplerise Trading Inc. is a Canadian brand since 2007. It is a renown dealer of kids and office furniture locally. Moreover, exporting electric fixtures e.g. switches, LED's, down-lights etc. to Middle East and Africa. We have initiated a number of steps including re-branding, to boost our export in 2020. We have successfully designed our new logo a few months ago through 'Artfolio' and now we are looking for an innovative idea for a letterhead.
Some key points:
• Red, black and white are the three colors used in all our packaging and furniture. (grey is optional)
• Shouldn’t be too wide.
• Use of watermark is preferable.
• You can visit our North American site at www.mapleriseinc.com. Export website of the company will be launched soon. www.mapleriseinc.ca
• Same letterhead will be used locally and internationally.
• Our new logo and sample packaging is attached.

```html
<!DOCTYPE html>
<html lang="en">
<head>
<meta charset="utf-8">
<title>Maplerise Trading Inc. — Business Card</title>
<link rel="stylesheet" href="https://fonts.googleapis.com/css2?family=Lato:wght@400;700&display=swap">
<style>
  :root {
    --page-bg: #dcd8d3;
    --card-bg: #f4f2ef;
    --card-edge: #cfcac4;
    --brand-red: #8e1b1e;
    --deep-red: #6f1214;
    --ink: #2e2e2e;
    --ink-soft: #3d3d3d;
    --swoosh-black: #1e1e1e;
  }
  html, body {
    margin: 0;
    padding: 0;
    width: 1200px;
    height: 970px;
    overflow: hidden;
    background: var(--page-bg);
  }
  .canvas {
    position: relative;
    width: 1200px;
    height: 970px;
  }
  .business-card {
    position: absolute;
    left: 100px;
    top: 205px;
    width: 1000px;
    height: 560px;
    background: linear-gradient(160deg, #f8f7f5 0%, var(--card-bg) 55%, #ebe8e4 100%);
    border: 1px solid var(--card-edge);
    box-shadow: 0 18px 40px rgba(0,0,0,0.18);
    overflow: hidden;
    font-family: "Lato", sans-serif;
    color: var(--ink);
  }
  .accent-bar {
    position: absolute;
    left: 0;
    top: 150px;
    width: 13px;
    height: 253px;
    background: var(--brand-red);
    border-radius: 0 3px 3px 0;
  }
  .contact-block {
    position: absolute;
    left: 52px;
    top: 150px;
  }
  .person-name {
    margin: 0;
    font-size: 29px;
    font-weight: 700;
    letter-spacing: 0.5px;
    color: var(--brand-red);
    line-height: 1.2;
  }
  .person-title {
    margin: 4px 0 0;
    font-size: 22px;
    color: var(--ink-soft);
  }
  .address {
    margin: 16px 0 0;
    font-size: 23px;
    line-height: 1.25;
    color: var(--ink-soft);
    font-style: normal;
  }
  .contact-list {
    list-style: none;
    margin: 24px 0 0;
    padding: 0;
  }
  .contact-list li {
    display: flex;
    align-items: center;
    gap: 18px;
    font-size: 23px;
    height: 34px;
    color: var(--ink-soft);
  }
  .contact-list svg {
    width: 20px;
    height: 20px;
    margin-left: 8px;
    fill: var(--brand-red);
  }
  .brand-lockup {
    position: absolute;
    left: 588px;
    top: 211px;
    display: flex;
    align-items: center;
    gap: 20px;
  }
  .brand-square {
    width: 96px;
    height: 96px;
    background: var(--brand-red);
    border-radius: 8px;
  }
  .brand-name {
    margin: 0;
    font-size: 40px;
    font-weight: 400;
    line-height: 1.08;
    letter-spacing: 2px;
    text-transform: uppercase;
    color: var(--ink);
  }
  .bottom-swoosh {
    position: absolute;
    left: 0;
    bottom: 0;
    width: 1000px;
    height: 90px;
  }
</style>
</head>
<body>
<div class="canvas">
  <section class="business-card">
    <div class="accent-bar"></div>

    <div class="contact-block">
      <h1 class="person-name">ALEX MORDEN</h1>
      <p class="person-title">CEO</p>
      <address class="address">245 Birchwood Ave, Unit 318<br>Oakridge Hill</address>
      <ul class="contact-list">
        <li>
          <svg viewBox="0 0 24 24" aria-hidden="true"><path d="M6.6 10.8a15.1 15.1 0 0 0 6.6 6.6l2.2-2.2a1 1 0 0 1 1-.25 11.4 11.4 0 0 0 3.6.57 1 1 0 0 1 1 1V20a1 1 0 0 1-1 1A17 17 0 0 1 3 4a1 1 0 0 1 1-1h3.5a1 1 0 0 1 1 1c0 1.25.2 2.45.57 3.57a1 1 0 0 1-.25 1z"/></svg>
          <span>+1 (888) 555-0142</span>
        </li>
        <li>
          <svg viewBox="0 0 24 24" aria-hidden="true"><path d="M2 5h20v14H2z M4 7v.5l8 5.5 8-5.5V7l-8 5.5z" fill-rule="evenodd"/></svg>
          <span>sales@mapleriseinc.com</span>
        </li>
        <li>
          <svg viewBox="0 0 24 24" aria-hidden="true"><path d="M12 2a10 10 0 1 0 0 20 10 10 0 0 0 0-20zm0 2a8 8 0 0 1 7.7 6H16a13 13 0 0 0-2-5.7A8 8 0 0 1 12 4zm-2.3.3A13 13 0 0 0 8 10H4.3a8 8 0 0 1 5.4-5.7zM4.3 14H8a13 13 0 0 0 1.7 5.7A8 8 0 0 1 4.3 14zM10 10a11 11 0 0 1 2-5 11 11 0 0 1 2 5zm0 4h4a11 11 0 0 1-2 5 11 11 0 0 1-2-5zm4.3 5.7A13 13 0 0 0 16 14h3.7a8 8 0 0 1-5.4 5.7z"/></svg>
          <span>www.mapleriseinc.ca</span>
        </li>
      </ul>
    </div>

    <div class="brand-lockup">
      <div class="brand-square"></div>
      <p class="brand-name">Maplerise<br>Trading</p>
    </div>

    <svg class="bottom-swoosh" viewBox="0 0 1000 90" preserveAspectRatio="none" aria-hidden="true">
      <path d="M400 90 C 560 40, 780 20, 1000 22 L1000 90 Z" fill="var(--brand-red)"/>
      <path d="M520 90 C 680 60, 850 48, 1000 50 L1000 90 Z" fill="var(--deep-red)"/>
      <path d="M380 88 C 560 26, 760 8, 950 6 C 760 14, 560 36, 400 90 Z" fill="var(--swoosh-black)"/>
    </svg>
  </section>
</div>
</body>
</html>
```